Mental Health Therapy Website

I need a design for a mental health therapy website. It is a private practice. The business name is Brindle Counseling, PLLC. My name is Martin Hale, LMHC, NCC, DCC. I would like some of the features/menus to be Home; Welcome/About Me, Rates and Services, Common Questions, and Contact.
If possible I would like a blog on the main page that I can update with articles I write. I would like the contact page to feature a map to my location (4318 Cedarbend Ave. E, Halden Falls, WA 98000).
I would like to place a small photo of me on the Welcome/About page.
I am new to this so if I am forgetting anything, please ask me!!
I will upload my logo so you can fit it and the color scheme into the design.
Thank you so very much!

```html
<!DOCTYPE html>
<html lang="en">
<head>
<meta charset="utf-8">
<title>Brindle Counseling</title>
<link href="https://fonts.googleapis.com/css2?family=Lato:ital,wght@0,300;0,400;0,700;0,900;1,400&display=swap" rel="stylesheet">
<style>
:root{
  --paper:#e2ddd5;
  --white:#ffffff;
  --ink:#1c1c1c;
  --muted:#8c8c8c;
  --body:#6f6f6f;
  --rule:#dcdcdc;
  --nav:#555555;
  --nav-active:#2f6aa3;
  --brand-blue:#2c5f92;
  --brand-green:#6a9a3a;
  --title-blue:#35506d;
  --band:#ececec;
  --field:#eef1f2;
  --icon-disc:#1f3a42;
}
*{box-sizing:border-box;margin:0;padding:0}
html,body{width:772px;height:1200px;overflow:hidden}
body{background:var(--paper);font-family:"Lato",sans-serif;color:var(--ink);position:relative}
.abs{position:absolute}
.sheet{left:85px;top:20px;width:603px;height:1068px;background:var(--white);box-shadow:0 0 10px rgba(0,0,0,.12)}

/* header */
.brand{left:105px;top:29px;display:flex;align-items:center;gap:5px}
.brand-dot{width:20px;height:20px;border-radius:50%;background:var(--brand-blue)}
.brand-name{font-size:12px;font-weight:700;color:var(--brand-blue)}
.nav{right:103px;top:35px;display:flex;gap:5px;font-size:9.2px;text-transform:uppercase;color:var(--nav)}
.nav .active{color:var(--nav-active)}

/* hero */
.hero{left:85px;top:62px;width:603px;height:206px;background:radial-gradient(circle at 78% 30%,#f4f4f4 0,#d9d9d9 45%,#c4c4c4 100%)}
.hero-figure{left:103px;top:62px;width:262px;height:206px;background:linear-gradient(180deg,#3a6aa0,#2e5c92)}
.hero-title{left:85px;width:650px;top:140px;text-align:center;font-size:34px;font-weight:900;color:#fff;text-shadow:1px 2px 3px rgba(0,0,0,.35);letter-spacing:-.5px}
.hero-title .amp{color:rgba(255,255,255,.55);font-weight:300}

/* section headings */
.heading{left:104px;width:565px;display:flex;align-items:center;gap:16px;font-size:18px;text-transform:uppercase}
.heading::before,.heading::after{content:"";flex:1;height:1px;background:var(--rule)}
.heading b{font-weight:900;color:var(--ink)}
.heading span{font-weight:300;color:var(--muted)}

/* services */
.divider{left:85px;width:603px;height:3px;background:linear-gradient(#d3d3d3,#f4f4f4)}
.service-disc{width:58px;height:58px;border-radius:50%;background:radial-gradient(circle at 40% 30%,#4d6a70,var(--icon-disc));top:326px;display:flex;align-items:center;justify-content:center}
.service-title{top:398px;width:140px;text-align:center;font-size:9px;font-weight:900;text-transform:uppercase}
.service-text{top:418px;width:132px;font-size:7.8px;line-height:12px;color:var(--body)}
.read-more{font-size:7px;font-style:italic;color:var(--body)}

/* works */
.works-band{left:85px;top:494px;width:603px;height:158px;background:var(--band)}
.work-thumb{top:559px;width:38px;height:38px;border-radius:50%;border:2px solid #fff;box-shadow:0 0 2px rgba(0,0,0,.3)}
.work-date{top:601px;width:40px;text-align:center;font-size:6.4px;color:var(--body)}
.work-title{top:559px;font-size:9px;font-weight:900;color:var(--title-blue);text-transform:uppercase}
.work-text{top:577px;width:128px;font-size:7.8px;line-height:12px;color:var(--body)}

/* contact */
.map{left:106px;top:741px;width:570px;height:176px;background:linear-gradient(135deg,#e9e5dc 0,#ece8df 60%,#e2ddd2 100%)}
.info{left:107px;font-size:7px;color:var(--body);display:flex;gap:5px;line-height:9px}
.info svg{flex:none}
.label{font-size:6.2px;color:var(--ink);text-transform:uppercase}
.field{background:var(--field)}
.send{left:598px;top:1043px;width:76px;height:19px;background:var(--brand-green);color:#fff;font-size:7px;font-weight:900;text-transform:uppercase;display:flex;align-items:center;justify-content:center;gap:5px}

/* footer */
.footer{left:104px;top:1125px;font-size:8.6px;line-height:12px;color:#333}
.footer b{font-weight:900}
.social{top:1124px;width:11px;height:11px;border-radius:50%;background:#444}
</style>
</head>
<body>
<div class="abs sheet"></div>

<header>
  <div class="abs brand"><span class="brand-dot"></span><span class="brand-name">Brindle Counseling</span></div>
  <nav class="abs nav">
    <span class="active">Home</span><span>About Me</span><span>Rates &amp; Service</span><span>Common Questions</span><span>Contact</span>
  </nav>
</header>

<section>
  <div class="abs hero" role="img" aria-label="Soft grey photo of a coffee cup"></div>
  <div class="abs hero-figure" role="img" aria-label="Blue silhouette of the therapist"></div>
  <h1 class="abs hero-title">HAPPY <span class="amp">&amp;</span> FULFILLED</h1>
</section>

<section>
  <div class="abs divider" style="top:266px"></div>
  <h2 class="abs heading" style="top:283px"><span><b>What</b> I serve?</span></h2>

  <div class="abs service-disc" style="left:140px" role="img" aria-label="Heart icon">
    <svg width="22" height="20" viewBox="0 0 22 20"><path d="M11 19 2 10a5 5 0 0 1 9-6 5 5 0 0 1 9 6z" fill="#fff"/></svg>
  </div>
  <div class="abs service-disc" style="left:285px" role="img" aria-label="Cloud icon">
    <svg width="26" height="18" viewBox="0 0 26 18"><path d="M6 17a5 5 0 0 1 0-10 7 7 0 0 1 13-1 5.5 5.5 0 0 1 1 11z" fill="#fff"/></svg>
  </div>
  <div class="abs service-disc" style="left:429px" role="img" aria-label="Chat icon">
    <svg width="26" height="20" viewBox="0 0 26 20"><ellipse cx="10" cy="8" rx="9" ry="6.5" fill="#fff"/><path d="M4 13 3 18l6-4z" fill="#fff"/><ellipse cx="18" cy="11" rx="7" ry="5" fill="#fff" stroke="#1f3a42" stroke-width="1.2"/></svg>
  </div>
  <div class="abs service-disc" style="left:574px" role="img" aria-label="Gear icon">
    <svg width="20" height="20" viewBox="0 0 20 20"><g fill="#fff"><circle cx="10" cy="10" r="6.5"/><rect x="8.2" y="0.5" width="3.6" height="19" rx="1"/><rect x="0.5" y="8.2" width="19" height="3.6" rx="1"/><rect x="8.2" y="0.5" width="3.6" height="19" rx="1" transform="rotate(45 10 10)"/><rect x="8.2" y="0.5" width="3.6" height="19" rx="1" transform="rotate(-45 10 10)"/></g><circle cx="10" cy="10" r="2.6" fill="#1f3a42"/></svg>
  </div>

  <h3 class="abs service-title" style="left:99px">Therapy for Individuals</h3>
  <h3 class="abs service-title" style="left:244px">Anxiety, Truama, Phobias</h3>
  <h3 class="abs service-title" style="left:388px">Consultations</h3>
  <h3 class="abs service-title" style="left:533px">Services</h3>

  <div class="abs service-text" style="left:104px">Vestibulum malesuada massa ut nisl ultrices vulputate. Curabitur ullamcorper faucibus pulvinar.<p class="read-more" style="margin-top:8px">read more ...</p></div>
  <div class="abs service-text" style="left:249px">At pretium eros varius. Maecenas bibendum, arcu scelerisque condimentum sagitti.<p class="read-more" style="margin-top:8px">read more...</p></div>
  <div class="abs service-text" style="left:393px">Maecenas bibendum, arcu scelerisque condimentum sagittis, enim purus tristique arcu, in egestas ante purus.<p class="read-more" style="margin-top:8px">read more...</p></div>
  <div class="abs service-text" style="left:538px;top:411px">Donec pharetra diam quis augue feugiat at pretium eros varius. Maecenas bibendum, arcu scelerisque.<p class="read-more" style="margin-top:8px">read more...</p></div>
</section>

<section>
  <div class="abs works-band"></div>
  <div class="abs divider" style="top:492px"></div>
  <div class="abs divider" style="top:650px"></div>
  <h2 class="abs heading" style="top:518px"><span><b>Latest</b> works</span></h2>

  <div class="abs work-thumb" style="left:104px;background:linear-gradient(#9fb3c4,#4c5a63)" role="img" aria-label="Photo of a pier"></div>
  <div class="abs work-thumb" style="left:297px;background:linear-gradient(#cfd6dc,#5e6a70)" role="img" aria-label="Photo of clouds over hills"></div>
  <div class="abs work-thumb" style="left:490px;background:linear-gradient(#a9b9c6,#51606a)" role="img" aria-label="Video thumbnail of a pier"></div>
  <div class="abs work-date" style="left:103px">SEP 17 2011</div>
  <div class="abs work-date" style="left:296px">SEP 17 2011</div>
  <div class="abs work-date" style="left:489px">SEP 17 2011</div>

  <h3 class="abs work-title" style="left:152px">Lorem ipsum dolor</h3>
  <h3 class="abs work-title" style="left:345px">Mauris in tellus magna</h3>
  <h3 class="abs work-title" style="left:538px">Fusce vitae elit es</h3>
  <p class="abs work-text" style="left:152px">Sit amet nec, consectetuer adipiscing elit. Aenean commodo ligula eget dolor.</p>
  <p class="abs work-text" style="left:345px">Curabitur purus est, semper ut elementum ut, tempus tincidunt ante. Nunc sit amet nisl turpis, ut lobortis purus.</p>
  <p class="abs work-text" style="left:538px">Sit amet nec, consectetuer adipiscing elit. Aenean commodo ligula eget dolor.</p>
</section>

<section>
  <h2 class="abs heading" style="top:683px"><span><b>Contact</b> info</span></h2>
  <div class="abs map" role="img" aria-label="Street map of the neighbourhood with the practice location marked"></div>

  <div class="abs info" style="top:927px">
    <svg width="9" height="8" viewBox="0 0 9 8"><path d="M4.5 0 9 4H7.8v4H5.5V5.5h-2V8H1.2V4H0z" fill="#666"/></svg>
    <span>1190 Harlow Street Fernvale South<br>Park, IN 46602</span>
  </div>
  <div class="abs info" style="top:954px">
    <svg width="9" height="9" viewBox="0 0 9 9"><rect x="2" y="0" width="5" height="9" rx="1" fill="#666"/><rect x="3" y="1.2" width="3" height="5.5" fill="#fff"/></svg>
    <span>+1 (555)-010-4471</span>
  </div>
  <div class="abs info" style="top:977px">
    <svg width="9" height="9" viewBox="0 0 9 9"><rect x="0" y="1.5" width="9" height="6" fill="#666"/><path d="M0 1.5 4.5 5 9 1.5" stroke="#fff" stroke-width=".8" fill="none"/></svg>
    <span>hello@brindlecounsel.example</span>
  </div>
  <div class="abs" style="left:243px;top:927px;width:1px;height:110px;background:var(--rule)"></div>

  <label class="abs label" style="left:253px;top:928px">Your Name*</label>
  <div class="abs field" style="left:253px;top:937px;width:132px;height:20px"></div>
  <label class="abs label" style="left:253px;top:966px">Your E-mail*</label>
  <div class="abs field" style="left:253px;top:975px;width:132px;height:20px"></div>
  <label class="abs label" style="left:253px;top:1005px">Your Website</label>
  <div class="abs field" style="left:253px;top:1014px;width:132px;height:19px"></div>
  <label class="abs label" style="left:396px;top:928px">Your Message*</label>
  <div class="abs field" style="left:396px;top:937px;width:278px;height:96px"></div>

  <div class="abs send">
    <svg width="9" height="7" viewBox="0 0 9 7"><rect width="9" height="7" fill="#fff"/><path d="M0 0 4.5 3.6 9 0" stroke="#6a9a3a" stroke-width=".9" fill="none"/></svg>
    Send Message
  </div>
</section>

<footer>
  <div class="abs footer">
    <b>BRINDLE</b> Counseling<br>
    +1 555 010 2290 &nbsp;|&nbsp; office@brindlecounsel.example<br>
    4318 Cedarbend Ave. E, Halden Falls, WA 98000.<br>
    © Copyright 2014
  </div>
  <span class="abs social" style="left:596px" aria-label="Social link"></span>
  <span class="abs social" style="left:625px" aria-label="Social link"></span>
  <span class="abs social" style="left:654px" aria-label="Social link"></span>
</footer>
</body>
</html>
```